Verdant Hollow Kukui Oil Label

We’re looking for a designer to develop a new label for our bottled Kukui oil. Final design files (including original file) would be provided to Verdant Hollow to make versions and updates as needed.

The label will be applied to a 4 ounce light amber PET Pavo round bottle (with a white disc top cap). Specs, content to include and more direction are provided in the provided brief.

Target Market(s)

Women and men, ages 25-49, who care about their skin and know what they do now is going to affect their skin as they age. They care about using natural products and want to know the ingredients. They’re aware of harmful ingredients (like parabens and phthalates), and if they aren’t aware, they want to be informed.

Their focus is on the overall value and experience provided by the product.

Industry/Entity Type

Skin Care Product

Font styles to use
Serif

Colors

Designer to choose colors to be used in the design.

Requirements
Must have
• The goal is to look simple and classic, and cater to men and women.
• Include the Verdant Hollow logo (either vertical or horizontal version)
• A UPC Code must be added to the box (location can be on the back lower corner). The size is 1.5 inches wide by .5 inches high. A code will be provided once a design draft is reviewed, since an annual cost will incur once a code is purchased.
• Messaging Requirements for label:
• Product Name:
• Kukui Oil
• Focal Point/Key Message:
• A superior moisturizer for the body, face and hair
• Include ingredients listing using a font size no less than 1/16” in height:
• Ingredients: Cold pressed kukui oil (aleurites moluccana), Vitamin E and phthalate-free lime fragrance.
•  
• List the product amount:
• 4.0 fl. oz. / 118 mL
• Include Directions for Use after or near Ingredients listing:
• Directions for Use: Apply a few drops as needed to your body, face or hair.
• Include Warnings after Directions. Lettering must be in bold type and in all CAPS on white background and may in no case be less than 1/16 inch in height:
• Warnings: For external use only. not recommended for those with nut allergies. Use as directed. Avoid contact with eyes. Keep out of reach of children.
• Include Website and contact info:
• VerdantHollow.com
• MADE IN U.S.A.
• Produced and distributed by Verdant HollowTM
• Maplewood, Ohio 43299
• Promotional copy to include:
• Kukui oil is widely used by the Hawaiian surfing community to help heal cuts, scrapes and sunburns. With high levels of linoleic and alpha-linolenic acids, this light oil deeply penetrates the skin’s tissues without leaving a greasy film.
• Other uses: An everyday moisturizer. Treats eczema and psoriasis. Removes make-up.
• (If this is too much copy, I can try and shorten the Promotional Copy and Other Uses sections)
Nice to have
• The flower from the logo represents “natural beauty” and we currently use it on its own and incorporate it as a design element. We’re open to enhancing the flower, using it in different ways or not using it on its own at all.
• Our current Website branding may be leveraged (verdanthollow.com):
• Font Family:
• Quattrocento (Normal 400)
• Back-up Font Family:
• Verdana, Geneva sans
• Headline color:
• Black #333333
• Body copy color:
• Gray #747474
Should not have
• What we don’t want:
• Too many colors
• Overly bright colors
• Photography

```html
<!DOCTYPE html>
<html lang="en">
<head>
<meta charset="utf-8">
<title>Verdant Hollow Kukui Oil Label</title>
<link rel="stylesheet" href="https://fonts.googleapis.com/css2?family=Oswald:wght@500&family=Roboto+Condensed:wght@400;700&display=swap">
<style>
  :root {
    --page: #ffffff;
    --label: #ffffff;
    --teal: #2aaac4;
    --teal-ink: #1a8fae;
    --ink: #231815;
    --body: #3d3d3d;
    --muted: #555555;
    --blossom: #f0a9a4;
    --white: #ffffff;
  }
  * { margin: 0; padding: 0; box-sizing: border-box; }
  html, body { width: 1200px; height: 884px; overflow: hidden; background: var(--page); }
  body { position: relative; font-family: "Roboto Condensed", Arial, sans-serif; color: var(--body); }

  .label {
    position: absolute; left: 190px; top: 115px; width: 847px; height: 637px;
    background: var(--label); box-shadow: 0 0 4px rgba(0,0,0,0.12); overflow: hidden;
  }
  .label > * { position: absolute; }

  .corner-bloom {
    left: 0; top: 0; width: 270px; height: 250px;
    background: radial-gradient(circle at 20px 20px, rgba(170,215,226,0.55) 0, rgba(200,230,237,0.35) 45%, rgba(255,255,255,0) 72%);
  }

  .promo {
    left: 20px; top: 120px; width: 245px; text-align: center; white-space: nowrap;
    font-size: 17.5px; line-height: 32.9px; color: var(--body);
  }
  .promo strong { color: var(--teal-ink); font-weight: 700; }

  .brand {
    left: 305px; top: 50px; width: 200px; display: flex; align-items: center; justify-content: center; gap: 6px;
    font-size: 30px; line-height: 1; color: var(--teal-ink); font-weight: 400; text-align: center;
  }
  .brand-name { width: 130px; }
  .brand-dot { width: 22px; height: 22px; border-radius: 50%; background: var(--blossom); flex: none; }

  .product-title {
    left: 282px; top: 184px; font-family: "Oswald", Impact, sans-serif; font-weight: 500;
    font-size: 64px; line-height: 66px; color: var(--ink); letter-spacing: 0;
  }
  .product-title .oil { display: block; font-size: 50px; line-height: 54px; }
  .tagline {
    left: 283px; top: 303px; white-space: nowrap; font-size: 17px; line-height: 20px; color: var(--muted);
  }
  .leaf-art {
    left: 400px; top: 215px; width: 142px; height: 175px;
    background: radial-gradient(ellipse at 60% 50%, rgba(42,170,196,0.18) 0, rgba(42,170,196,0.06) 55%, rgba(255,255,255,0) 75%);
  }

  .facts { left: 545px; width: 280px; text-align: center; white-space: nowrap; font-size: 17.5px; line-height: 23px; color: var(--body); }
  .facts h2 { font-size: 17.5px; font-weight: 400; color: var(--teal-ink); line-height: 23px; }
  .ingredients { top: 59px; }
  .directions { top: 177px; }
  .warnings { top: 281px; font-size: 16px; line-height: 23px; text-transform: uppercase; color: var(--body); }

  .band { left: 0; top: 431px; width: 847px; height: 206px; background: var(--teal); color: var(--white); }
  .band > * { position: absolute; }
  .band-bloom {
    left: 250px; top: 0; width: 360px; height: 206px;
    background: radial-gradient(circle at 180px 90px, rgba(255,255,255,0.14) 0, rgba(255,255,255,0.06) 50%, rgba(255,255,255,0) 72%);
  }
  .other-uses { left: 42px; top: 26px; width: 200px; text-align: center; white-space: nowrap; font-size: 17.5px; line-height: 23px; }
  .free-tag {
    left: 283px; top: 25px; padding: 5px 0 7px; font-size: 18px; line-height: 20px;
    border-top: 2px solid var(--white); border-bottom: 2px solid var(--white);
  }
  .net-volume { left: 290px; top: 127px; width: 235px; text-align: center; font-size: 17.5px; }
  .maker { left: 575px; top: 25px; width: 230px; text-align: center; }
  .made-in { font-size: 17.5px; line-height: 22px; }
  .producer { margin-top: 8px; font-size: 15.5px; line-height: 18.5px; }
  .site { margin-top: 18px; font-size: 19.5px; font-weight: 700; letter-spacing: 0.8px; }
</style>
</head>
<body>
  <main class="label">
    <div class="corner-bloom" role="img" aria-label="Faint line-drawn flower decoration"></div>

    <p class="promo"><strong>Kukui nut oil</strong> is widely<br>used by the Hawaiian surfing<br>community to help heal cuts,<br>scrapes and sunburns. With<br>high levels of linoleic and<br>alpha-linolenic acids, this<br>light oil deeply penetrates<br>the skin’s tissues without<br>leaving a greasy film.</p>

    <div class="brand">
      <span class="brand-name">Verdant Hollow</span>
      <span class="brand-dot"></span>
    </div>

    <h1 class="product-title">KUKUI<span class="oil">OIL</span></h1>
    <p class="tagline">A superior<br>moisturizer for<br>the body, face and hair</p>
    <div class="leaf-art" role="img" aria-label="Line-drawn leaf sprig illustration"></div>

    <section class="facts ingredients">
      <h2>Ingredients:</h2>
      <p>Cold pressed kukui oil (aleurites<br>moluccana), Vitamin E and<br>phthalate-free lime fragrance.</p>
    </section>
    <section class="facts directions">
      <h2>Directions for Use:</h2>
      <p>Apply a few drops as needed to<br>your body, face or hair.</p>
    </section>
    <p class="facts warnings">Warnings: For external use<br>only. Not recommended for<br>those with nut allergies. Use<br>as directed. Avoid contact<br>with eyes. Keep out of reach of<br>children.</p>

    <footer class="band">
      <div class="band-bloom" role="img" aria-label="Faint flower decoration on teal band"></div>
      <p class="other-uses">Other uses: An<br>everyday moisturizer.<br>Treats eczema and<br>psoriasis. Removes<br>make-up.</p>
      <p class="free-tag">Phthalate-free</p>
      <p class="net-volume">4.0 fl. oz. / 118 mL</p>
      <div class="maker">
        <p class="made-in">MADE IN U.S.A.</p>
        <p class="producer">Produced and distributed by<br>Verdant HollowTM<br>Maplewood, Ohio 43299</p>
        <p class="site">VerdantHollow.com</p>
      </div>
    </footer>
  </main>
</body>
</html>
```